VELTRIX GROUP
Project: VXG LOGO
VXG LOGO - Trade
VXG LOGO
Use same font as used in my logo
FAISAL NOORi
GENERAL MANAGER
RIYADH
info@veltrixgroup-example.com
VXGROUP VXGROUP
following changes on your design no #158 the logo upper and left side of the letter head company name bottom and left side of the letter haead The business cards are also in the above pattern. waiting for your immediate response. thanks.

```html
<!DOCTYPE html>
<html lang="en">
<head>
<meta charset="utf-8">
<title>Veltrix Group Stationery</title>
<link href="https://fonts.googleapis.com/css2?family=Montserrat:wght@400;600&display=swap" rel="stylesheet">
<style>
  :root {
    --backdrop: #2e2e2e;
    --paper: #ffffff;
    --brand-blue: #2f5aa6;
    --label: #ffffff;
  }
  html, body {
    margin: 0;
    padding: 0;
    width: 1200px;
    height: 1002px;
    overflow: hidden;
    background: var(--backdrop);
    font-family: "Montserrat", Arial, sans-serif;
  }
  .stage { position: relative; width: 1200px; height: 1002px; }

  .brand-mark {
    position: absolute;
    display: flex;
    align-items: center;
    color: var(--brand-blue);
    font-weight: 600;
    line-height: 1;
  }
  .brand-mark .mark-square {
    display: block;
    background: var(--brand-blue);
  }

  .business-card {
    position: absolute;
    left: 89px; top: 260px;
    width: 344px; height: 195px;
    background: var(--paper);
    color: var(--brand-blue);
  }
  .business-card .brand-mark { left: 8px; top: 12px; gap: 8px; font-size: 26px; }
  .business-card .mark-square { width: 30px; height: 30px; }
  .business-card .company-name {
    position: absolute; left: 8px; top: 66px;
    font-size: 11px; font-weight: 600; letter-spacing: 0.3px;
  }
  .person {
    position: absolute; right: 10px; top: 88px;
    width: 168px; text-align: right;
  }
  .person-name {
    font-size: 12px; letter-spacing: 0.4px;
    border-bottom: 1.5px solid var(--brand-blue);
    padding-bottom: 2px;
  }
  .person-title { font-size: 7px; font-weight: 600; margin-top: 3px; letter-spacing: 0.3px; }

  .contact { position: absolute; font-size: 10px; line-height: 15px; color: var(--brand-blue); }
  .contact .row { display: flex; align-items: center; gap: 4px; }
  .contact svg { width: 8px; height: 8px; fill: var(--brand-blue); }
  .business-card .contact { left: 8px; top: 127px; }

  .letterhead {
    position: absolute;
    left: 531px; top: 54px;
    width: 604px; height: 807px;
    background: var(--paper);
  }
  .letterhead .brand-mark { left: 33px; top: 48px; gap: 12px; font-size: 40px; }
  .letterhead .mark-square { width: 46px; height: 46px; }
  .letterhead .contact { left: 35px; top: 735px; }

  .sheet-label {
    position: absolute;
    left: 531px; top: 870px; width: 604px;
    text-align: center;
    color: var(--label);
    font-size: 44px; font-weight: 400;
  }
</style>
</head>
<body>
<div class="stage">
  <section class="business-card">
    <div class="brand-mark"><span class="mark-square"></span>VXG</div>
    <div class="company-name">VELTRIX GROUP</div>
    <div class="person">
      <div class="person-name">FAISAL NOORi</div>
      <div class="person-title">GENERAL MANAGER</div>
    </div>
    <div class="contact">
      <div class="city">RIYADH</div>
      <div class="row"><svg viewBox="0 0 10 10"><path d="M2 0h2l1 3-1.5 1a6 6 0 0 0 2.5 2.5L7 5l3 1v2c0 1-1 2-2 2A8 8 0 0 1 0 2c0-1 1-2 2-2z"/></svg>966-400-1234</div>
      <div class="row"><svg viewBox="0 0 10 10"><path d="M2 0h6v3H2zM0 3h10v5H8v2H2V8H0zM3 6v3h4V6z"/></svg>966-400-5678</div>
      <div class="row"><svg viewBox="0 0 10 10"><path d="M0 2h10v6H0zM1 3v.5l4 2.5 4-2.5V3L5 5.5z"/></svg>info@veltrixgroup-example.com</div>
    </div>
  </section>

  <section class="letterhead">
    <div class="brand-mark"><span class="mark-square"></span>VXG</div>
    <div class="contact">
      <div class="city">RIYADH</div>
      <div class="row"><svg viewBox="0 0 10 10"><path d="M2 0h2l1 3-1.5 1a6 6 0 0 0 2.5 2.5L7 5l3 1v2c0 1-1 2-2 2A8 8 0 0 1 0 2c0-1 1-2 2-2z"/></svg>966-400-1234</div>
      <div class="row"><svg viewBox="0 0 10 10"><path d="M2 0h6v3H2zM0 3h10v5H8v2H2V8H0zM3 6v3h4V6z"/></svg>966-400-5678</div>
      <div class="row"><svg viewBox="0 0 10 10"><path d="M0 2h10v6H0zM1 3v.5l4 2.5 4-2.5V3L5 5.5z"/></svg>info@veltrixgroup-example.com</div>
    </div>
  </section>

  <div class="sheet-label">Letterhead</div>
</div>
</body>
</html>
```